Create a capturing book cover for The Hollow Lantern

Book Title: The Hollow Lantern
Subtitle: Rising Beyond the Restless Tide
Author: Marlowe Quintessa

Synopsis of book:
She didn’t really know what she wanted to do, but she knew she wanted to be successful. She struggled with identifying with what she was passionate about and what her purpose was for her life. Fear, turmoil, relationships, and career paths created turbulence in her long journey to fulfill her vision and lifetime goals. The Hollow Lantern exemplifies women who struggle with these things. The Hollow Lantern digs into the crevices of a blurry vision, disturbed, and fearful woman.

-The book focuses on a woman who is not necessarily physically cripple, but mentally, spiritually, and emotionally crippled.

The photos attached are just examples (not all have to be used)

Target Market(s)

Women who are dealing with barriers that are holding them back from reaching their goals or being successful

Font styles to use
Serif
Sans Serif

Colors
6b449b
b7a5cd

Requirements
Must have
• purple incorporated (not the full cover)
• I would like an African American woman, dominican woman, or mixed (you cannot tell what ethnicity she is) on the front cover if any.
Nice to have
• I would like the cover to tell the story. My ideas were maybe an actual crippled woman looking into the mirror at a woman who is at peace, or two women in one that shows one struggling and one living in happiness, or a crippled woman with her back turned and a path with something that symbolizes happiness at the end, or a lady sitting on the floor kind of distraught. I really want the designer to be creative. I do not have an exact image of what I want it to look like. These are just ideas. They do not have to be within the realms that I mentioned.
Should not have
• Extravagant text
• cartoon or animated pictures
• do not want a dark cover

```html
<!DOCTYPE html>
<html lang="en">
<head>
<meta charset="utf-8">
<title>The Hollow Lantern — Book Cover</title>
<link rel="stylesheet" href="https://fonts.googleapis.com/css2?family=Josefin+Sans:wght@300;400&family=Parisienne&display=swap">
<style>
  :root {
    --backdrop: #c4c4c4;
    --purple-deep: #3f1d55;
    --purple-mid: #6b449b;
    --purple-soft: #b7a5cd;
    --mist: #f1edf5;
    --ink: #2e1440;
    --white: #ffffff;
  }
  * { margin: 0; padding: 0; box-sizing: border-box; }
  html, body { width: 1200px; height: 1000px; overflow: hidden; }
  body { background: var(--backdrop); position: relative; }

  .back-cover, .spine, .front-cover {
    position: absolute; top: 177px; height: 671px; overflow: hidden;
  }
  .back-cover { left: 143px; width: 424px; }
  .spine { left: 587px; width: 29px; }
  .front-cover { left: 636px; width: 424px; }

  .cover-art { position: absolute; inset: 0; }
  .back-cover .cover-art {
    background:
      radial-gradient(ellipse 60% 45% at 45% 40%, var(--mist) 0%, rgba(241,237,245,0.85) 45%, rgba(183,165,205,0) 80%),
      linear-gradient(160deg, var(--purple-soft) 0%, var(--mist) 35%, var(--purple-soft) 70%, var(--purple-mid) 100%);
  }
  .spine .cover-art {
    background: linear-gradient(180deg, var(--mist) 0%, var(--purple-soft) 30%, var(--purple-mid) 60%, var(--purple-deep) 100%);
  }
  .front-cover .cover-art {
    background:
      radial-gradient(ellipse 45% 30% at 55% 25%, var(--mist) 0%, rgba(241,237,245,0) 100%),
      linear-gradient(150deg, var(--purple-soft) 0%, var(--mist) 25%, var(--purple-mid) 55%, var(--purple-deep) 80%);
  }

  .base-band {
    position: absolute; left: 0; right: 0; bottom: 0; height: 18px;
    background: var(--purple-mid);
  }

  .synopsis {
    position: absolute; left: 40px; top: 144px; width: 350px;
    font-family: "Josefin Sans", sans-serif; font-weight: 400;
    font-variant: small-caps; font-size: 14px; letter-spacing: 1.2px;
    line-height: 20px; color: var(--ink); text-align: center;
  }

  .spine-title, .spine-author {
    position: absolute; left: 50%; white-space: nowrap;
    transform-origin: center; transform: translate(-50%, -50%) rotate(90deg);
  }
  .spine-title {
    top: 140px; font-family: "Parisienne", cursive; font-size: 18px; color: var(--ink);
  }
  .spine-author {
    top: 535px; font-family: "Josefin Sans", sans-serif; font-variant: small-caps;
    font-size: 17px; letter-spacing: 1.5px; color: var(--ink);
  }

  .title-block { position: absolute; left: 34px; top: 140px; width: 380px; }
  .title-lead {
    display: block; font-family: "Parisienne", cursive; font-size: 22px;
    color: var(--ink); margin-left: 2px; line-height: 20px;
  }
  .book-title {
    font-family: "Parisienne", cursive; font-weight: 400; font-size: 44px;
    color: var(--ink); line-height: 44px; margin-left: 18px;
  }
  .subtitle {
    margin: 14px 0 0 58px; font-family: "Parisienne", cursive; font-weight: 400;
    font-size: 25px; line-height: 26px; color: var(--white);
    -webkit-text-stroke: 0.6px var(--purple-mid);
  }
  .subtitle .second-line { display: block; margin-left: 48px; }
  .subtitle small { font-size: 15px; }

  .author {
    position: absolute; left: 0; right: 0; top: 588px; text-align: center;
    font-family: "Josefin Sans", sans-serif; font-weight: 300;
    font-variant: small-caps; font-size: 38px; letter-spacing: 2.5px; color: var(--white);
  }
</style>
</head>
<body>
  <section class="back-cover">
    <div class="cover-art" role="img" aria-label="Washed purple photograph of bare branches in the rain over a blurred figure"></div>
    <p class="synopsis">She didn’t really know what she wanted to do, but she knew she wanted to be successful. She struggled with identifying with what she was passionate about and what her purpose was for her life. Fear, turmoil, relationships, and career paths created turbulence in her long journey to fulfill her vision and lifetime goals. The Hollow Lantern exemplifies women who struggle with these things. The Hollow Lantern digs into the crevices of a blurry vision, disturbed, and fearful woman.</p>
    <div class="base-band"></div>
  </section>

  <section class="spine">
    <div class="cover-art" role="img" aria-label="Continuation of the purple rain-washed photograph"></div>
    <span class="spine-title">The Hollow Lantern</span>
    <span class="spine-author">Marlowe Quintessa</span>
  </section>

  <section class="front-cover">
    <div class="cover-art" role="img" aria-label="Purple-toned photograph of a woman seen through a rain-streaked window with bare branches"></div>
    <div class="title-block">
      <span class="title-lead">The</span>
      <h1 class="book-title">Hollow Lantern</h1>
      <h2 class="subtitle">Rising Beyond<span class="second-line"><small>the</small> Restless Tide</span></h2>
    </div>
    <p class="author">Marlowe Quintessa</p>
    <div class="base-band"></div>
  </section>
</body>
</html>
```